Redesign of Brochure of company services

We need a redesign a brochure. All of the content on the existing brochure correct, but the design we are not pleased with it. I will provide the previous brochure. Every Window Bright is Angolan company that provides multiple service ranging providing fruits, vegetables, fisheries, and meat to multiple industries in angola. Every Window Bright seeks to start delivering or providing their service to home owners looking for fresh products. We want a brochure design that covers all of these aspects.

Target Market(s)

Home owners, middle and upper age mothers, middle and upper class

Industry/Entity Type

Retail

Requirements
Must have
• Logo of the company and the content info
Nice to have
• It's up to you

```html
<!DOCTYPE html>
<html lang="pt">
<head>
<meta charset="utf-8">
<title>Every Window Bright – Brochura (verso)</title>
<link href="https://fonts.googleapis.com/css2?family=Arimo:wght@400;700&display=swap" rel="stylesheet">
<style>
  :root{
    --stage:#000;
    --green:#4caf50;
    --green-dark:#2f9a45;
    --green-light:#6cc24a;
    --ribbon:#62b957;
    --orange:#f26b22;
    --orange-soft:#f7923a;
    --blue:#1d8fcf;
    --bar-green:#5fa85a;
    --ink:#111;
    --white:#fff;
  }
  *{box-sizing:border-box;margin:0;padding:0}
  html,body{width:1200px;height:1200px;overflow:hidden;background:var(--stage);font-family:"Arimo",Arial,sans-serif}
  .canvas{position:relative;width:1200px;height:1200px}
  .sheet{position:absolute;left:55px;top:116px;width:1098px;height:853px;background:var(--white);overflow:hidden}
  .abs{position:absolute}

  /* ribbons */
  .ribbon{position:absolute;width:118px;height:118px}
  .ribbon svg{position:absolute;inset:0}
  .ribbon span{position:absolute;left:0;right:0;top:20px;text-align:center;color:var(--white);font-size:15px;line-height:20px}

  /* left panel */
  .panel-left{position:absolute;left:0;top:0;width:365px;height:853px;background:linear-gradient(#fff,#ececec)}
  .photo-produce{left:0;top:0;width:365px;height:209px;background:linear-gradient(135deg,#a8683a,#c98b52 45%,#8f5a34)}
  .lead-title{left:37px;top:227px;color:var(--orange-soft);font-size:23px;font-weight:700}
  .lead-body{left:37px;top:264px;width:310px;font-size:18px;line-height:19.5px;color:var(--ink)}
  .step{left:0;height:31px;color:var(--white);font-size:20px;font-weight:700;line-height:31px;padding-left:42px}
  .step svg{position:absolute;left:40px;top:9px}
  .step b{padding-left:24px}
  .step-phone{top:355px;width:322px;background:var(--blue)}
  .step-bank{top:388px;width:320px;background:var(--bar-green)}
  .step-receive{top:421px;width:322px;background:var(--orange-soft)}
  .producer-note{left:39px;top:474px;width:300px;font-size:18px;line-height:22px;color:var(--ink)}
  .photo-cattle{left:0;top:563px;width:180px;height:181px;background:linear-gradient(#9cc0dc,#7a9a5c 45%,#6a5a3a)}
  .photo-farmer{left:184px;top:563px;width:181px;height:181px;background:linear-gradient(135deg,#4f7a3a,#2e4a22 60%,#3b2a1e)}
  .left-footer{left:0;top:744px;width:365px;height:109px;background:linear-gradient(var(--green-light),var(--green-dark));text-align:center;color:var(--white)}
  .left-footer p{font-size:20px;margin-top:26px}
  .left-footer strong{display:block;font-size:23px;color:var(--ink)}

  /* right spread */
  .spread{position:absolute;left:365px;top:0;width:733px;height:853px}
  .field{left:0;top:240px;width:733px;height:400px;background:linear-gradient(#cfe6b0 0%,#6aa63a 8%,#4f8f2a 18%,#7cc43a 30%,#5aa52a 70%,#3f8a22 100%)}
  .green-base{left:0;top:480px;width:733px;height:373px}
  .offer-title{left:75px;top:149px;color:var(--orange);font-size:19px;font-weight:700}
  .offer-body{left:75px;top:172px;font-size:14px;line-height:19px;font-weight:700;font-variant:small-caps;color:var(--ink);letter-spacing:.3px}
  .brand-main{left:390px;top:44px;width:310px;text-align:center;font-size:30px;color:#222;white-space:nowrap}
  .brand-main i{display:block;width:70px;height:70px;margin:0 auto 44px;background:var(--orange)}
  .values{left:0;top:364px;width:370px;text-align:center;color:var(--white);font-size:39px;font-weight:700;line-height:41px;letter-spacing:1px}
  .brand-small{left:158px;top:636px;width:82px;height:80px;background:var(--white);text-align:center;font-size:12px;line-height:13px;color:#222;padding-top:14px}
  .brand-small i{display:block;width:22px;height:22px;margin:0 auto 6px;background:var(--orange)}
  .contact{left:0;top:724px;width:380px;text-align:center;color:var(--white)}
  .contact .place{font-size:23px}
  .contact .phone{font-size:25px;font-weight:700;color:var(--ink);line-height:26px}
  .contact .mail{font-size:18px;font-weight:700;margin-top:4px}
  .products{left:385px;top:602px;width:333px;text-align:center;color:var(--orange);font-size:37px;font-weight:700;line-height:41px;text-shadow:-2px -2px 0 #fff,2px -2px 0 #fff,-2px 2px 0 #fff,2px 2px 0 #fff}
  .tagline{left:385px;top:744px;width:333px;text-align:center;color:var(--white);font-size:23px;line-height:24px}

  .caption{position:absolute;left:0;right:0;top:995px;text-align:center;color:var(--white);font-size:46px}
</style>
</head>
<body>
<main class="canvas">
  <article class="sheet">

    <section class="panel-left">
      <div class="abs photo-produce" role="img" aria-label="Legumes e frutas frescos sobre mesa de madeira"></div>
      <div class="ribbon" style="left:27px;top:14px">
        <svg width="118" height="118" viewBox="0 0 118 118"><polygon points="0,0 118,0 118,114 59,88 0,114" fill="var(--ribbon)" stroke="#fff" stroke-width="3"/></svg>
        <span>Frescos<br>de<br>Qualidade</span>
      </div>
      <h2 class="abs lead-title">Confie em Qualidade</h2>
      <p class="abs lead-body">A qualidade de todos os frescos distribuídospor nós é verificada para que apenas os produtos aprovados cheguem até si.</p>
      <div class="abs step step-phone"><svg width="16" height="14" viewBox="0 0 16 14"><path d="M1 7l5 5L15 1" fill="none" stroke="var(--bar-green)" stroke-width="3"/></svg><b>Encomende por telefone</b></div>
      <div class="abs step step-bank"><svg width="16" height="14" viewBox="0 0 16 14"><path d="M1 7l5 5L15 1" fill="none" stroke="var(--orange-soft)" stroke-width="3"/></svg><b>Pague no banco</b></div>
      <div class="abs step step-receive"><svg width="16" height="14" viewBox="0 0 16 14"><path d="M1 7l5 5L15 1" fill="none" stroke="var(--blue)" stroke-width="3"/></svg><b>Receba os seus frescos</b></div>
      <p class="abs producer-note">Se for produtor e deseja comercializar os seus produtosde forma segura, contacte-nos hoje!</p>
      <div class="abs photo-cattle" role="img" aria-label="Gado a pastar no campo"></div>
      <div class="abs photo-farmer" role="img" aria-label="Agricultor a carregar um cesto de frutas"></div>
      <footer class="abs left-footer">
        <p>Manuseamos com cuidado<strong>+244 900 410 275</strong></p>
      </footer>
    </section>

    <section class="spread">
      <div class="abs field" role="img" aria-label="Campo verde de cultivo ao pôr do sol"></div>
      <svg class="abs green-base" width="733" height="373" viewBox="0 0 733 373">
        <defs>
          <linearGradient id="base" x1="0" y1="0" x2="0" y2="1"><stop offset="0" stop-color="#5cbb4a"/><stop offset="1" stop-color="#2f9a45"/></linearGradient>
          <linearGradient id="silver" x1="0" y1="0" x2="1" y2="0"><stop offset="0" stop-color="#fff"/><stop offset="0.6" stop-color="#f4f4f4"/><stop offset="1" stop-color="#b8b8b8"/></linearGradient>
        </defs>
        <path d="M240 126 C420 112 590 22 733 29 L733 69 C600 60 450 115 300 124 Z" fill="url(#silver)"/>
        <path d="M0 29 C90 110 200 130 300 124 C450 115 600 60 733 69 L733 373 L0 373 Z" fill="url(#base)"/>
      </svg>
      <div class="ribbon" style="left:38px;top:14px">
        <svg width="118" height="120" viewBox="0 0 118 120"><polygon points="0,0 118,0 118,116 59,90 0,116" fill="var(--ribbon)" stroke="#fff" stroke-width="3"/></svg>
        <span style="top:30px">Entregamos<br>à sua porta</span>
      </div>
      <h3 class="abs offer-title">FAZEMOS DESCONTOS</h3>
      <p class="abs offer-body">Fazemos descontos a<br>clientes com contratos de<br>fornecimento contínuo</p>
      <div class="abs brand-main"><i></i>Every Window Bright</div>
      <h1 class="abs values">QUALIDADE<br>RAPIDEZ<br>SATISFAÇÃO</h1>
      <div class="abs brand-small"><i></i>Every Window Bright</div>
      <address class="abs contact" style="font-style:normal">
        <div class="place">Rua das Acácias, Luanda</div>
        <div class="phone">+244 900 410 275</div>
        <div class="mail">contacto@everywindowbright.ao</div>
      </address>
      <h2 class="abs products">Hortaliças<br>Frutas Carnes<br>Peixes Mariscos</h2>
      <p class="abs tagline">Levamos produtos frescos<br>Nacionais à sua porta.</p>
    </section>

  </article>
  <p class="caption">Back Side</p>
</main>
</body>
</html>
```